Korvane Motors business cards

We need business cards for our company Korvane Motors, based in Brisbane but trading world wide. We buy and sell Korvane Motors, generators and marine equipment. The design needs to be kept clean, simple but eye catching.
Please keep with our current logo (included) and further information can be included on request

Business

0792cd
33a6d7
85cae6
3276b5
0455a3
cedeed
cee9f5
ffffff

```html
<!DOCTYPE html>
<html lang="en">
<head>
<meta charset="utf-8">
<title>Korvane Motors – Business Cards</title>
<link href="https://fonts.googleapis.com/css2?family=Roboto:wght@400;500&display=swap" rel="stylesheet">
<style>
  :root {
    --brand-blue: #4585c0;
    --swoosh-grey: #7d8084;
    --card-white: #ffffff;
    --backdrop: #e4e6e8;
    --ink-light: #ffffff;
  }
  html, body {
    margin: 0;
    padding: 0;
    width: 1200px;
    height: 771px;
    overflow: hidden;
    background: var(--backdrop);
    font-family: "Roboto", sans-serif;
  }
  .canvas {
    position: relative;
    width: 1200px;
    height: 771px;
  }
  .card {
    position: absolute;
    top: 235px;
    width: 520px;
    height: 300px;
    background: var(--card-white);
    box-shadow: 0 4px 14px rgba(0,0,0,0.12);
    overflow: hidden;
  }
  .card--front { left: 50px; }
  .card--back { left: 630px; }

  .wordmark {
    position: absolute;
    display: flex;
    align-items: flex-start;
    gap: 14px;
    color: var(--brand-blue);
  }
  .wordmark__square {
    width: 74px;
    height: 74px;
    border-radius: 10px;
    background: var(--brand-blue);
    flex: none;
  }
  .wordmark__name {
    font-weight: 400;
    font-size: 38px;
    line-height: 36px;
    margin: 0;
  }
  .wordmark__suffix {
    display: block;
    text-align: right;
    font-size: 13px;
    line-height: 18px;
    font-weight: 400;
  }
  .card--front .wordmark { left: 92px; top: 82px; }
  .card--back .wordmark { left: 200px; top: 26px; }
  .card--back .wordmark__square { width: 58px; height: 58px; border-radius: 8px; }
  .card--back .wordmark__name { font-size: 31px; line-height: 30px; }
  .card--back .wordmark__suffix { font-size: 11px; }

  .band { position: absolute; inset: 0; }

  .contact-list {
    position: absolute;
    left: 22px;
    top: 138px;
    margin: 0;
    padding: 0;
    list-style: none;
    color: var(--ink-light);
    font-size: 10px;
    letter-spacing: 0.8px;
    line-height: 15px;
  }
  .contact-list li { display: flex; align-items: center; gap: 7px; }
  .contact-list__icon {
    width: 9px;
    height: 9px;
    border-radius: 50%;
    background: var(--ink-light);
    flex: none;
  }
  .contact-list__indent { padding-left: 16px; }

  .holder {
    position: absolute;
    right: 24px;
    bottom: 22px;
    text-align: right;
    color: var(--ink-light);
    text-transform: uppercase;
  }
  .holder__name { font-size: 15px; letter-spacing: 2px; font-weight: 500; }
  .holder__role { font-size: 10px; letter-spacing: 2.5px; margin-top: 3px; }
</style>
</head>
<body>
<main class="canvas">

  <section class="card card--front" aria-label="Card front">
    <div class="wordmark">
      <span class="wordmark__square"></span>
      <div>
        <h1 class="wordmark__name">Korvane<br>Motors</h1>
        <span class="wordmark__suffix">Pty Ltd</span>
      </div>
    </div>
  </section>

  <section class="card card--back" aria-label="Card back">
    <svg class="band" width="520" height="300" viewBox="0 0 520 300" aria-hidden="true">
      <path d="M0,100 C190,102 390,168 520,230 L520,250 C380,190 180,118 0,115 Z" fill="var(--swoosh-grey)"/>
      <path d="M0,115 C180,118 380,190 520,250 L520,300 L0,300 Z" fill="var(--brand-blue)"/>
    </svg>

    <div class="wordmark">
      <span class="wordmark__square"></span>
      <div>
        <h2 class="wordmark__name">Korvane<br>Motors</h2>
        <span class="wordmark__suffix">Pty Ltd</span>
      </div>
    </div>

    <ul class="contact-list">
      <li><span class="contact-list__icon"></span>Suite # 118, Quay Bldg.,</li>
      <li class="contact-list__indent">QLD 4000</li>
      <li><span class="contact-list__icon"></span>07-3155-0148</li>
      <li><span class="contact-list__icon"></span>07-3155-0262</li>
      <li><span class="contact-list__icon"></span>04-1877-3390</li>
      <li><span class="contact-list__icon"></span>daniel@korvanemotors.au</li>
      <li class="contact-list__indent">www.korvanemotors.au</li>
    </ul>

    <div class="holder">
      <div class="holder__name">Daniel Reyes</div>
      <div class="holder__role">Owner / C.E.O</div>
    </div>
  </section>

</main>
</body>
</html>
```